Business Card Design Project for Architecture and Interior Design company

We need a business card design and logo for an architecture and design firm located in Santiago de Chile. It´s a small company, and the name is "Ostrevo" ("Ostr" from my surname Ostrini, and "arq" for arquitectura or architecture. But it would also be nice that the logo comunicates de Word game "Bella" as beautiful in italian, and "arq" as architecture".
The idea is to give a delicate, elegant and sofisticated, yet fresh image. Would prefer grey black and white colors, but wouldn´t mind to use another additional color.
I allready have a web page www.ostrevo-studio.example, but would like to improve the logo design.
Please contact if any further information is requiered.
Reason: Need a more arquitectural and desing spirit in the cards. Few of them give that idea.

```html
<!DOCTYPE html>
<html lang="es">
<head>
<meta charset="utf-8">
<title>Ostrevo – Tarjetas de presentación</title>
<link rel="stylesheet" href="https://fonts.googleapis.com/css2?family=Questrial&display=swap">
<style>
  :root {
    --backdrop: #e4e4e2;
    --card: #f4f4f3;
    --card-edge: #d9d9d7;
    --ink: #2b2b2b;
    --ink-soft: #6e6e6e;
    --rule: #8a8a8a;
    --accent: #cf1840;
    --pattern-a: #efefed;
    --pattern-b: #e6e6e3;
  }
  * { box-sizing: border-box; margin: 0; padding: 0; }
  html, body {
    width: 1200px;
    height: 927px;
    overflow: hidden;
    background: var(--backdrop);
    font-family: "Questrial", "Century Gothic", sans-serif;
    color: var(--ink);
  }
  .sheet {
    position: relative;
    width: 1200px;
    height: 927px;
  }
  .card {
    position: absolute;
    top: 308px;
    width: 540px;
    height: 310px;
    background: var(--card);
    border: 1px solid var(--card-edge);
    box-shadow: 0 6px 18px rgba(0,0,0,0.12);
    overflow: hidden;
  }
  .card--front { left: 45px; }
  .card--back { left: 615px; }

  /* Front */
  .front__marker {
    position: absolute;
    left: 70px; top: 68px;
    width: 4px; height: 32px;
    background: var(--ink);
  }
  .front__spine {
    position: absolute;
    left: 71px; top: 100px;
    width: 1px; height: 140px;
    background: var(--rule);
  }
  .front__name {
    position: absolute;
    left: 104px; top: 50px;
    font-size: 22px;
    letter-spacing: 0.5px;
    color: var(--ink);
    white-space: nowrap;
  }
  .front__role {
    position: absolute;
    left: 236px; top: 86px;
    font-size: 14px;
    letter-spacing: 7px;
    color: var(--accent);
  }
  .front__contact {
    position: absolute;
    left: 86px; top: 136px;
    list-style: none;
    font-size: 15px;
    line-height: 29px;
    color: var(--ink);
  }
  .front__rule {
    position: absolute;
    left: 86px; top: 163px;
    width: 250px; height: 1px;
    background: var(--rule);
  }
  .front__hatch {
    position: absolute;
    left: 346px; top: 157px;
  }
  .front__logo {
    position: absolute;
    right: 40px; bottom: 32px;
    font-size: 27px;
    letter-spacing: 1px;
    color: var(--ink-soft);
  }

  /* Back */
  .back__pattern {
    position: absolute;
    inset: 0;
    background: linear-gradient(135deg, var(--pattern-a) 0%, var(--pattern-b) 55%, var(--pattern-a) 100%);
  }
  .back__brand {
    position: absolute;
    left: 0; right: 0; top: 112px;
    text-align: center;
  }
  .back__logo {
    font-size: 46px;
    letter-spacing: 2px;
    color: var(--ink-soft);
    line-height: 1;
  }
  .back__tagline {
    margin-top: 8px;
    font-size: 9.5px;
    letter-spacing: 1.5px;
    color: var(--ink-soft);
  }
</style>
</head>
<body>
<main class="sheet">
  <section class="card card--front" aria-label="Tarjeta, anverso">
    <div class="front__marker"></div>
    <div class="front__spine"></div>
    <h1 class="front__name">MIRA OSTRINI KELMAR</h1>
    <p class="front__role">ARQUITECTO</p>
    <div class="front__rule"></div>
    <svg class="front__hatch" width="160" height="12" viewBox="0 0 160 12" aria-hidden="true">
      <g stroke="#8a8a8a" stroke-width="1.2">
        <line x1="2" y1="11" x2="8" y2="1"/><line x1="9" y1="11" x2="15" y2="1"/>
        <line x1="16" y1="11" x2="22" y2="1"/><line x1="23" y1="11" x2="29" y2="1"/>
        <line x1="30" y1="11" x2="36" y2="1"/><line x1="37" y1="11" x2="43" y2="1"/>
        <line x1="44" y1="11" x2="50" y2="1"/><line x1="51" y1="11" x2="57" y2="1"/>
        <line x1="58" y1="11" x2="64" y2="1"/><line x1="65" y1="11" x2="71" y2="1"/>
        <line x1="72" y1="11" x2="78" y2="1"/><line x1="79" y1="11" x2="85" y2="1"/>
        <line x1="86" y1="11" x2="92" y2="1"/><line x1="93" y1="11" x2="99" y2="1"/>
        <line x1="100" y1="11" x2="106" y2="1"/><line x1="107" y1="11" x2="113" y2="1"/>
        <line x1="114" y1="11" x2="120" y2="1"/><line x1="121" y1="11" x2="127" y2="1"/>
        <line x1="128" y1="11" x2="134" y2="1"/><line x1="135" y1="11" x2="141" y2="1"/>
        <line x1="142" y1="11" x2="148" y2="1"/><line x1="149" y1="11" x2="155" y2="1"/>
      </g>
    </svg>
    <ul class="front__contact">
      <li>+56 9 5550 1234</li>
      <li>mostrini@ostrevo-studio.example</li>
      <li>www.ostrevo-studio.example</li>
    </ul>
    <p class="front__logo">OSTREVO</p>
  </section>

  <section class="card card--back" aria-label="Tarjeta, reverso">
    <div class="back__pattern" role="img" aria-label="Patrón de líneas geométricas finas en gris claro"></div>
    <div class="back__brand">
      <p class="back__logo">OSTREVO</p>
      <p class="back__tagline">ARQUITECTURA | DISEÑO DE INTERIORES</p>
    </div>
  </section>
</main>
</body>
</html>
```